BRIVON - Business Card Design Project

We need a business card design for a consultant company called BRIVON, LLC. (stands for Bright Retail Inventory Venture Operations Network). The company provides Information Technology solutions, custom applications, services for financial and supply chain worldwide and focuses on business IT process improvements and all the steps leading to the procurement or integrating of any Enterprise related systems.

Industry/Entity Type

Financial

Requirements
Must have
• - In the submitted proposed version you should have one variant with black background and one with white.
The designer should show the shadow element of the company name in binary code (010000100101001001001001010101100100111101001110). It can be in one line or split in two

In your example please use the following info
Peter Dorne
Principal Consultant
pdorne@brivonhq.net
+1 (555) 014 - 2298

Please keep in mind that the design should have some spaces to add the second phone and/or web site name
Nice to have
• Since this IT company and is working closely with Accounting and Logistics Application you can add some elements (contour only) of these types of the bussines as well (for example some $ or euro sign or truck or warehouse element)
Should not have
• Don’t use any extra color that is not in the company color logo pattern

```html
<!DOCTYPE html>
<html lang="en">
<head>
<meta charset="utf-8">
<title>BRIVON – Business Cards</title>
<link rel="stylesheet" href="https://fonts.googleapis.com/css2?family=Arimo:wght@400&family=Open+Sans:wght@400;700&display=swap">
<style>
  :root {
    --page: #d9d9d9;
    --white: #ffffff;
    --black: #000000;
    --ink: #111111;
    --accent: #f7a21b;
    --mark: #1f6fb5;
    --dark-card: #000000;
    --dark-panel: #0b0b0b;
    --dark-binary: #2e2e2e;
    --dark-rule: #bdbdbd;
    --light-card: #ffffff;
    --light-panel: #f1f1f1;
  }
  * { margin: 0; padding: 0; box-sizing: border-box; }
  html, body { width: 954px; height: 1200px; overflow: hidden; }
  body { background: var(--page); position: relative; font-family: "Open Sans", Arial, sans-serif; }

  .card {
    position: absolute; left: 76px; width: 796px; height: 456px;
    border-radius: 28px; overflow: hidden;
  }
  .card--dark { --card-bg: var(--dark-card); --panel-bg: var(--dark-panel); --text: var(--white); }
  .card--light { --card-bg: var(--light-card); --panel-bg: var(--light-panel); --text: var(--ink); box-shadow: 0 2px 10px rgba(0,0,0,0.18); }
  .card { background: var(--card-bg); }
  .card--front { top: 86px; }
  .card--back { top: 642px; }

  .card__panel { position: absolute; background: var(--panel-bg); }
  .card--front .card__panel { left: 61px; top: 20px; width: 689px; height: 218px; }
  .card--back .card__panel { left: 61px; top: 63px; width: 689px; height: 253px; }

  .brand { position: absolute; left: 93px; }
  .card--front .brand { top: 70px; }
  .card--back .brand { top: 134px; }
  .brand__dot {
    position: absolute; left: 0; top: 0; width: 130px; height: 130px;
    border-radius: 50%; background: var(--mark);
  }
  .brand__name {
    position: absolute; left: 176px; top: 0;
    font-family: "Arimo", Arial, sans-serif; font-weight: 400;
    font-size: 80px; line-height: 80px; color: var(--text); letter-spacing: 1px;
    white-space: nowrap;
  }
  .brand__tagline {
    position: absolute; left: 177px; top: 73px;
    font-family: "Arimo", Arial, sans-serif; font-size: 15.5px; color: var(--text);
    white-space: nowrap;
  }

  .person { position: absolute; left: 269px; top: 220px; }
  .person__name { font-weight: 700; font-size: 22px; line-height: 30px; color: var(--accent); }
  .person__title { font-size: 17px; line-height: 26px; color: var(--text); }

  .contact-rule { position: absolute; left: 480px; top: 210px; width: 1px; height: 98px; background: var(--dark-rule); }
  .contact { position: absolute; left: 502px; top: 206px; list-style: none; }
  .contact li { font-size: 17.5px; line-height: 26.3px; color: var(--text); white-space: nowrap; }

  .binary { position: absolute; left: 12px; top: 330px; }
  .binary text { font-family: "Open Sans", Arial, sans-serif; font-weight: 700; font-size: 54px; fill: var(--dark-binary); }

  .web-address {
    position: absolute; left: 258px; top: 313px;
    font-size: 22px; letter-spacing: 7px; color: var(--accent);
  }
</style>
</head>
<body>

<section class="card card--dark card--front" aria-label="Business card, black variant, front">
  <div class="card__panel"></div>
  <div class="brand">
    <span class="brand__dot" aria-hidden="true"></span>
    <span class="brand__name">BRIVON</span>
    <span class="brand__tagline">Bright Retail Inventory Venture Operations Network</span>
  </div>
  <div class="person">
    <p class="person__name">Peter Dorne</p>
    <p class="person__title">Principal Consultant</p>
  </div>
  <div class="contact-rule"></div>
  <ul class="contact">
    <li>P. +1 (555) 014 - 2298</li>
    <li>P. +1 (555) 014 - 2298</li>
    <li>W. www.brivonhq.com</li>
    <li>E. pdorne@brivonhq.net</li>
  </ul>
  <svg class="binary" width="770" height="120" viewBox="0 0 770 120" aria-label="BRIVON in binary">
    <text x="0" y="50" textLength="760" lengthAdjust="spacingAndGlyphs">010000100101001001001001</text>
    <text x="0" y="102" textLength="760" lengthAdjust="spacingAndGlyphs">010101100100111101001110</text>
  </svg>
</section>

<section class="card card--light card--back" aria-label="Business card, white variant">
  <div class="card__panel"></div>
  <div class="brand">
    <span class="brand__dot" aria-hidden="true"></span>
    <span class="brand__name">BRIVON</span>
    <span class="brand__tagline">Bright Retail Inventory Venture Operations Network</span>
  </div>
  <p class="web-address">www.brivonhq.com</p>
</section>

</body>
</html>
```